Income Tax Flyer - Updates Needed

Just need to update this flyer design and give it a new look. We would like to keep all the same wording but make it stand out a little more. Our selling point is the "Same Day Tax Advance up to $6,000"

Industry/Entity Type

Lending, Small Loans, Tax Services, Title Loans, Personal Loans

```html
<!DOCTYPE html>
<html lang="en">
<head>
<meta charset="utf-8">
<title>Tax Advance Flyer</title>
<link rel="stylesheet" href="https://fonts.googleapis.com/css2?family=Carlito:wght@400;700&family=Montserrat:wght@500;600;700&family=Open+Sans:wght@800&display=swap">
<style>
  :root {
    --page-bg: #d4d4d4;
    --paper: #ffffff;
    --green-light: #8dc63f;
    --green-mid: #4fb848;
    --green-main: #0aa551;
    --green-deep: #0b5e33;
    --red: #c4161c;
    --photo-warm: #d9cbbd;
    --photo-cool: #c9d0d3;
  }
  * { margin: 0; padding: 0; box-sizing: border-box; }
  html, body { width: 1200px; height: 1200px; overflow: hidden; }
  body { background: var(--page-bg); position: relative; font-family: "Montserrat", sans-serif; }

  .flyer {
    position: absolute; left: 160px; top: 29px;
    width: 881px; height: 1142px;
    background: var(--paper); overflow: hidden;
  }
  .hero-photo {
    position: absolute; left: 0; top: 71px; width: 881px; height: 603px;
    background: linear-gradient(100deg, var(--photo-cool) 0%, var(--photo-warm) 35%, #eef0ef 60%, #b89a8a 85%, #8e6f63 100%);
  }
  .hero-shapes { position: absolute; left: 0; top: 0; width: 881px; height: 1142px; }

  .brand-box {
    position: absolute; left: 276px; top: 8px; width: 328px; height: 174px;
    background: var(--paper);
    box-shadow: 0 4px 4px rgba(0,0,0,.35);
    display: flex; align-items: center; justify-content: center; gap: 12px;
  }
  .brand-mark { width: 22px; height: 22px; border-radius: 50%; background: var(--green-deep); flex: none; }
  .brand-name {
    font-family: "Carlito", sans-serif; font-weight: 700; font-size: 34px; line-height: 1.05;
    color: var(--green-deep); text-align: left;
  }

  .headline {
    position: absolute; left: 0; width: 881px; text-align: center;
    font-family: "Open Sans", sans-serif; font-weight: 800; color: var(--red);
    text-shadow: 1px 2px 0 #7d0d10, 2px 4px 5px rgba(0,0,0,.35);
    letter-spacing: 1px;
  }
  .headline-top { top: 510px; font-size: 64px; padding-left: 0px; }
  .headline-amount { top: 585px; font-size: 70px; }

  .advance-band {
    position: absolute; left: 0; top: 674px; width: 881px; height: 131px;
    background: var(--green-main); color: #fff; text-align: center;
    font-family: "Carlito", sans-serif; font-size: 50px; line-height: 60px; padding-top: 6px;
  }
  .advance-band strong { font-weight: 700; }

  .feature {
    position: absolute; top: 805px; width: 260px; text-align: center;
    color: var(--green-deep); font-weight: 600; font-size: 25px; line-height: 33px;
  }
  .feature svg { display: block; margin: 0 auto; }
  .feature-speed { left: 76px; }
  .feature-amount { left: 321px; }
  .feature-easy { left: 586px; }
  .feature-label { margin-top: 22px; }

  .contact-wave { position: absolute; left: 0; top: 990px; width: 881px; height: 152px; }
  .contact-callout {
    position: absolute; left: 0; width: 881px; text-align: center;
    font-weight: 700; font-size: 22px; color: var(--red);
    -webkit-text-stroke: 0; text-shadow: 0 0 2px #fff, 0 0 2px #fff, 0 0 3px #fff;
  }
  .callout-cta { top: 1021px; }
  .callout-phone { top: 1048px; }
  .address-row {
    position: absolute; left: 0; top: 1070px; width: 881px; height: 60px;
    display: flex; align-items: center; justify-content: center;
    color: #fff; font-weight: 500; font-size: 28px;
  }
  .address-row span { padding: 0 20px; }
  .address-divider { width: 3px; height: 60px; background: #fff; }
</style>
</head>
<body>
<main class="flyer">
  <div class="hero-photo" role="img" aria-label="Photo of two smiling women in a bright office"></div>

  <svg class="hero-shapes" viewBox="0 0 881 1142" aria-hidden="true">
    <polygon points="0,490 62,429 163,523 0,632" fill="#8dc63f"/>
    <polygon points="0,632 317,419 381,518 70,674 0,674" fill="#4fb848"/>
    <polygon points="70,674 640,414 667,524 201,674" fill="#0aa551"/>
    <polygon points="201,674 881,470 881,674" fill="#ffffff"/>
  </svg>

  <div class="brand-box">
    <span class="brand-mark"></span>
    <span class="brand-name">Keystone<br>Lending Group</span>
  </div>

  <h1 class="headline headline-top">APPLY HERE FOR</h1>
  <h2 class="headline headline-amount">$5,000-$6,000 TODAY!</h2>

  <section class="advance-band">
    <p>File Your Taxes And Apply For An</p>
    <p><strong>Easy Advance!</strong></p>
  </section>

  <div class="feature feature-speed">
    <svg width="86" height="96" viewBox="0 0 86 96" fill="none" stroke="#0b5e33" stroke-width="6">
      <circle cx="43" cy="54" r="36"/>
      <circle cx="43" cy="54" r="22" stroke-width="3"/>
      <rect x="36" y="2" width="14" height="10" rx="4" stroke-width="4"/>
      <line x1="43" y1="12" x2="43" y2="18"/>
      <line x1="10" y1="22" x2="16" y2="28" stroke-width="7"/>
      <line x1="76" y1="22" x2="70" y2="28" stroke-width="7"/>
      <text x="43" y="64" text-anchor="middle" font-family="Montserrat, sans-serif" font-size="28" font-weight="700" fill="#0b5e33" stroke="none">$</text>
    </svg>
    <p class="feature-label">Available In<br>24 Hours or Less</p>
  </div>

  <div class="feature feature-amount">
    <svg width="116" height="96" viewBox="0 0 116 96" fill="none" stroke="#0b5e33" stroke-width="4" stroke-linecap="round" stroke-linejoin="round">
      <path d="M40 64 C16 62 4 50 4 36 C4 18 26 4 52 4 C76 4 96 16 96 34"/>
      <path d="M58 82 L44 70 C40 66 44 60 50 62 L58 68 L58 34 C58 28 68 28 68 34 L68 52 L96 58 C106 60 108 68 106 76 L102 92"/>
      <text x="44" y="46" text-anchor="middle" font-family="Montserrat, sans-serif" font-size="26" font-weight="700" fill="#0b5e33" stroke="none">$</text>
    </svg>
    <p class="feature-label">Choose Your<br>Loan Amount</p>
  </div>

  <div class="feature feature-easy">
    <svg width="80" height="96" viewBox="0 0 80 96" fill="none" stroke="#0b5e33" stroke-width="4" stroke-linejoin="round">
      <rect x="4" y="2" width="48" height="78" rx="5"/>
      <rect x="12" y="10" width="32" height="50"/>
      <path d="M20 60 L8 60 C2 60 2 70 8 70 L22 70 M8 70 C2 70 2 80 8 80 L22 80"/>
      <path d="M52 44 L74 64 L62 80 L62 94 L28 94 L28 80"/>
    </svg>
    <p class="feature-label">Quick And<br>Easy</p>
  </div>

  <svg class="contact-wave" viewBox="0 0 881 152" preserveAspectRatio="none" aria-hidden="true">
    <path d="M0 10 C120 22 260 28 420 22 C560 16 700 28 881 36 L881 152 L0 152 Z" fill="#8dc63f"/>
    <path d="M0 4 C160 20 300 20 440 14 C600 8 700 18 760 26" stroke="#8dc63f" stroke-width="2" fill="none" opacity=".7"/>
  </svg>

  <p class="contact-callout callout-cta">Contact Us Today!</p>
  <p class="contact-callout callout-phone">Phone Numbrer</p>

  <div class="address-row">
    <span>Address Line 1</span>
    <i class="address-divider"></i>
    <span>Address Line 2</span>
    <i class="address-divider"></i>
    <span>Address Line 3</span>
  </div>
</main>
</body>
</html>
```